Long Term Contract - Wordpress Designers Wanted!

We are rapidly growing start-up web development company, focused on website development geared towards the insurance industry.

To increase our impact, we’ve decided to add a freelance designer to the team to assist in graphical elements and webdesign for our clients and template development.

This is to screen for a LONG TERM relationship where we will work together to design and develop sites for insurance agents. We are seeking a talented web designer with experience in WordPress and WordPress theme development to work his/her magic on our new websites.

To win this contest, please create an example website design for an individual insurance agent that sells auto and home insurance. The website will essentially be a "business card" for the agent and will generate trust, show experience, and most importantly create a call to action for the person to call or get a quote.

An example is here:

http://plovermarsh.example/heron/

As part of the deliverable, we will want you to integrate these templates as child themes under Quillmorph "Trellis" template framework - which we can provide you of course. All forms should be done in gravity forms.

Target Market(s)

Audience: consumers shopping for insurance agent

Industry/Entity Type

Insurance

Requirements
Must have
• Pages:
-home
-products
-about
-news/blog
-Contact us

On home page the following elements should be included:
-contact us form
-agent contact information
-blog entries
-testimonial
-agency overview
Should not have
• flash

```html
<!DOCTYPE html>
<html lang="en">
<head>
<meta charset="utf-8">
<title>Insurance Agent</title>
<link rel="stylesheet" href="https://fonts.googleapis.com/css2?family=Ubuntu:wght@400;500;700&family=Open+Sans:wght@400;600&display=swap">
<style>
:root{
  --crimson:#c0074a;
  --crimson-dark:#8e0535;
  --ink:#333;
  --muted:#666;
  --panel:#f3f3f3;
  --bg:#ececec;
  --header-top:#6a6a6a;
  --header-bottom:#3f3f3f;
  --nav-ink:#555;
}
*{box-sizing:border-box;margin:0;padding:0}
html,body{width:923px;height:1200px;overflow:hidden}
body{background:var(--bg);font-family:'Open Sans',Arial,sans-serif;color:var(--ink);position:relative}
.abs{position:absolute}
.site-header{left:0;top:0;width:923px;height:87px;background:linear-gradient(#747474,var(--header-bottom))}
.brand{left:53px;top:18px;font-family:'Ubuntu',sans-serif;font-weight:700;font-size:28px;color:#fff;letter-spacing:1px}
.main-nav a{position:absolute;top:100px;font-family:'Ubuntu',sans-serif;font-weight:500;font-size:14px;color:var(--nav-ink);text-decoration:none}
.nav-active{left:69px;top:80px;width:85px;height:53px;background:linear-gradient(var(--crimson),var(--crimson-dark))}
.nav-active span{position:absolute;left:0;right:0;top:20px;text-align:center;color:#fff;font-family:'Ubuntu',sans-serif;font-weight:500;font-size:14px}
.video-frame{left:48px;top:157px;width:382px;height:260px;background:#fff;border:1px solid #ccc;padding:6px}
.video-still{width:369px;height:228px;background:linear-gradient(135deg,#cfd6dc,#8aa6c6 55%,#c9a27c)}
.video-bar{width:369px;height:20px;background:#2a2a2a;color:#ddd;font-size:8px;display:flex;align-items:center;padding:0 8px;gap:8px}
.video-bar .track{flex:1;height:3px;background:#666;position:relative}
.video-bar .track i{position:absolute;left:0;top:0;width:45%;height:3px;background:#aaa}
.play-btn{left:188px;top:248px}
.intro h1{position:absolute;left:451px;top:152px;font-family:'Ubuntu',sans-serif;font-weight:700;font-size:17px;line-height:20px;color:var(--crimson)}
.intro p{position:absolute;left:451px;top:203px;width:402px;font-size:9.7px;line-height:15px;color:var(--ink)}
.quote-form{left:446px;top:277px;width:424px;height:140px;background:#e3e3e3;border:1px solid #ddd}
.quote-form h2{position:absolute;left:13px;top:8px;font-family:'Ubuntu',sans-serif;font-weight:700;font-size:14.5px;color:var(--crimson)}
.quote-form .lede{position:absolute;left:13px;top:28px;font-size:8.4px;color:#444}
.field{position:absolute;height:19px;width:151px;border-radius:10px;background:#fff;border:1px solid #d6d6d6;font-size:9.5px;color:#555;padding:3px 9px}
.key-art{left:349px;top:46px;width:57px;height:50px;border-radius:6px;background:linear-gradient(#d8d8d8,#a8a8a8)}
.submit{left:350px;top:106px;width:61px;height:21px;border-radius:10px;background:linear-gradient(var(--crimson),var(--crimson-dark));color:#fff;font-family:'Ubuntu',sans-serif;font-weight:700;font-size:10px;text-align:center;line-height:21px}
.rule-dotted{left:44px;top:454px;width:834px;border-top:1px dotted #999}
.product{position:absolute;top:450px;width:200px}
.product .tab{display:inline-block;margin-left:8px;height:24px;padding:4px 8px 0;background:linear-gradient(var(--crimson),var(--crimson-dark));color:#fff;font-family:'Ubuntu',sans-serif;font-weight:700;font-size:13px}
.product .thumb{margin-top:15px;width:194px;height:82px;border-radius:10px;background:#fff;border:1px solid #ddd;padding:4px}
.product .thumb div{width:100%;height:100%;border-radius:6px}
.product p{margin-top:15px;font-size:9.3px;line-height:16.8px;color:#444;text-align:justify}
.product .more{position:absolute;right:0;top:225px;width:71px;height:20px;border-radius:10px;background:linear-gradient(#666,#2b2b2b);border:2px solid #ddd;color:#fff;font-family:'Ubuntu',sans-serif;font-weight:700;font-size:9px;text-align:center;line-height:16px}
.col-sep{position:absolute;top:455px;height:240px;border-left:1px dotted #999}
.rule-soft{left:51px;top:732px;width:818px;border-top:1px solid #d5d5d5}
.posts{left:42px;top:759px;width:558px;height:380px;background:var(--panel)}
.posts-title{left:106px;top:777px;font-family:'Ubuntu',sans-serif;font-weight:700;font-size:18.5px;color:var(--crimson)}
.posts-title span{color:#333}
.post{position:absolute;width:520px}
.post .date{position:absolute;left:-56px;top:-18px}
.post h3{font-family:'Open Sans',sans-serif;font-weight:400;font-size:14px;color:var(--crimson);letter-spacing:.4px}
.post .meta{font-size:10px;color:#888;margin-top:1px}
.post .body{font-size:8.8px;line-height:15px;color:#444;text-align:justify;margin-top:6px}
.post .byline{font-size:10px;color:#666;margin-top:7px}
.post .byline b{color:var(--crimson);font-weight:400}
.post .share{display:flex;align-items:center;gap:3px;font-size:10px;color:#666;margin-top:8px}
.share i{display:inline-block;width:14px;height:14px;border:1px solid #aaa;background:#e6e6e6}
.post .more-info{position:absolute;right:0;bottom:0;font-size:10px;color:var(--crimson)}
.contact{left:621px;top:760px;width:250px;font-size:9.4px;line-height:15px;color:#333}
.contact h2{font-family:'Ubuntu',sans-serif;font-weight:700;font-size:15px;color:var(--crimson);margin-bottom:8px}
.contact h4{font-weight:600;font-size:10.5px;color:var(--crimson)}
.contact a{color:var(--crimson)}
.rule-dashed{left:611px;top:977px;width:255px;border-top:1px dashed #bbb}
.testimonial{left:609px;top:991px;width:253px;height:125px;border-radius:18px;background:linear-gradient(var(--crimson),var(--crimson-dark));color:#fff;padding:11px 17px}
.testimonial h2{font-family:'Ubuntu',sans-serif;font-weight:700;font-size:15px;margin-bottom:7px}
.testimonial p{font-size:8.6px;line-height:15px;text-align:justify}
.quote-tail{left:780px;top:1114px}
.attribution{left:650px;top:1127px;font-size:9px;color:#333}
.site-footer{left:0;top:1158px;width:923px;height:42px;background:linear-gradient(var(--crimson),var(--crimson-dark));display:flex;justify-content:center;align-items:center;gap:15px;padding-right:52px;color:#fff;font-family:'Ubuntu',sans-serif;font-weight:500;font-size:9.5px}
</style>
</head>
<body>

<header class="abs site-header"></header>
<div class="abs brand">Insurance Agent</div>

<nav class="main-nav">
  <div class="abs nav-active"><span>HOME</span></div>
  <a style="left:179px">PRODUCTS</a>
  <a style="left:316px">ABOUT US</a>
  <a style="left:446px">NEWS/BLOG</a>
  <a style="left:597px">CONTACT US</a>
</nav>

<div class="abs video-frame">
  <div class="video-still" role="img" aria-label="Video still of a smiling agent at a home office desk with a laptop"></div>
  <div class="video-bar"><span>■</span><span>❚❚</span><span class="track"><i></i></span><span>00:38/01:29</span><span>◀) ▤ ‹› ✉</span></div>
</div>
<svg class="abs play-btn" width="64" height="64" viewBox="0 0 64 64" aria-hidden="true">
  <circle cx="32" cy="32" r="29" fill="#333" fill-opacity=".85" stroke="#eee" stroke-width="3"/>
  <path d="M25 19 L46 32 L25 45 Z" fill="#fff"/>
</svg>

<section class="intro">
  <h1>Answer your retirement questions here at<br>Insurance Agent</h1>
  <p>We serve New Hampshire, Massachusetts and Maine with the best in insurance and investments advice. Get free, professional advice on how to protect your money using customized financial tools, including:</p>
</section>

<form class="abs quote-form">
  <h2>Call Us At 1-877-555-0142 For A Free Consultation</h2>
  <p class="lede">I can help you sort through your options and will review current coverage, at no cost to you.</p>
  <div class="field" style="left:13px;top:66px">First Name :</div>
  <div class="field" style="left:176px;top:66px">Last Name :</div>
  <div class="field" style="left:13px;top:99px">Phone :</div>
  <div class="field" style="left:176px;top:99px">Email :</div>
  <div class="abs key-art" role="img" aria-label="Illustration of a puzzle piece with a key"></div>
  <div class="abs submit">SUBMIT</div>
</form>

<div class="abs rule-dotted"></div>
<div class="col-sep" style="left:251px"></div>
<div class="col-sep" style="left:460px"></div>
<div class="col-sep" style="left:669px"></div>

<article class="product" style="left:46px">
  <span class="tab">Long Term Care</span>
  <div class="thumb"><div role="img" aria-label="Photo of a multi-generation family meeting an advisor" style="background:linear-gradient(90deg,#e8d8c8,#b9c8d8)"></div></div>
  <p>Lorem ipsum dolor sit amet, consectetuer adipiscing elit, sed diam nonummy nibh euismod tincidunt ut laoreet dolore magna aliquam erat volutpat. Ut wisi</p>
  <span class="more">Readmore</span>
</article>
<article class="product" style="left:256px">
  <span class="tab">Medicare Plans</span>
  <div class="thumb"><div role="img" aria-label="Photo of a medical benefits claim form with a calculator" style="background:linear-gradient(90deg,#d8d8d8,#f4f4f4)"></div></div>
  <p>Lorem ipsum dolor sit amet, consectetuer adipiscing elit, sed diam nonummy nibh euismod tincidunt ut laoreet dolore magna aliquam erat volutpat. Ut wisi</p>
  <span class="more">Readmore</span>
</article>
<article class="product" style="left:466px">
  <span class="tab">Life and Health</span>
  <div class="thumb"><div role="img" aria-label="Photo of a family relaxing together on a bed" style="background:linear-gradient(90deg,#e2d6cc,#f3eee9)"></div></div>
  <p>Lorem ipsum dolor sit amet, consectetuer adipiscing elit, sed diam nonummy nibh euismod tincidunt ut laoreet dolore magna aliquam erat volutpat. Ut wisi</p>
  <span class="more">Readmore</span>
</article>
<article class="product" style="left:675px">
  <span class="tab">Fixed Annuities</span>
  <div class="thumb"><div role="img" aria-label="Photo of a couple shaking hands with an advisor" style="background:linear-gradient(90deg,#d9c9b2,#9fb4c8)"></div></div>
  <p>Lorem ipsum dolor sit amet, consectetuer adipiscing elit, sed diam nonummy nibh euismod tincidunt ut laoreet dolore magna aliquam erat volutpat. Ut wisi</p>
  <span class="more">Readmore</span>
</article>

<div class="abs rule-soft"></div>

<section class="abs posts"></section>
<svg class="abs" style="left:53px;top:764px" width="46" height="46" viewBox="0 0 46 46" aria-hidden="true">
  <line x1="6" y1="44" x2="20" y2="6" stroke="#999" stroke-width="2"/>
  <path d="M20 6 L44 12 L34 26 L14 22 Z" fill="#e04a26"/>
  <circle cx="29" cy="16" r="5" fill="#fff"/>
</svg>
<div class="abs posts-title">Recent <span>Posts</span></div>

<svg width="0" height="0" style="position:absolute">
  <defs>
    <g id="date-badge">
      <path d="M26 0 L31 5 L38 2 L40 9 L47 9 L46 16 L52 20 L48 26 L52 32 L46 36 L47 43 L40 43 L38 50 L31 47 L26 52 L21 47 L14 50 L12 43 L5 43 L6 36 L0 32 L4 26 L0 20 L6 16 L5 9 L12 9 L14 2 L21 5 Z" fill="#c0074a"/>
      <path d="M6 34 L46 34 L47 43 L40 43 L38 50 L31 47 L26 52 L21 47 L14 50 L12 43 L5 43 Z" fill="#222"/>
    </g>
  </defs>
</svg>

<article class="post" style="left:85px;top:828px">
  <svg class="date" width="52" height="72" viewBox="0 0 52 72"><use href="#date-badge"/><text x="26" y="14" fill="#fff" font-size="9" text-anchor="middle" font-family="Open Sans">Dec</text><text x="26" y="29" fill="#fff" font-size="13" font-weight="700" text-anchor="middle" font-family="Ubuntu">13th</text><text x="26" y="44" fill="#fff" font-size="9" font-weight="700" text-anchor="middle" font-family="Open Sans">2011</text></svg>
  <h3>Most Americans don’t have retirement plan</h3>
  <div class="meta">Posted on September 15, 2011 by admin</div>
  <p class="body">Lorem Ipsum is simply dummy text of the printing and typesetting industry. Lorem Ipsum has been the industry's standard dummy text ever since the 1500s, when an unknown printer took a galley of type and scrambled it to make a type specimen book. It has survived not only five centuries, but also the leap into electronic typesetting, remaining essentially unchanged. Lorem Ipsum is simply dummy text of the printing and typesetting industry.</p>
  <div class="byline"><b>[Blog Psted By</b> Mara Dellow<b>]</b></div>
  <div class="share">Share This <i></i><i></i><i></i><i></i></div>
  <span class="more-info">More info [+]</span>
</article>

<article class="post" style="left:76px;top:994px">
  <svg class="date" width="52" height="72" viewBox="0 0 52 72"><use href="#date-badge"/><text x="26" y="14" fill="#fff" font-size="9" text-anchor="middle" font-family="Open Sans">Dec</text><text x="26" y="29" fill="#fff" font-size="13" font-weight="700" text-anchor="middle" font-family="Ubuntu">13th</text><text x="26" y="44" fill="#fff" font-size="9" font-weight="700" text-anchor="middle" font-family="Open Sans">2011</text></svg>
  <h3>Most Americans don’t have retirement plan</h3>
  <div class="meta">Posted on September 15, 2011 by admin</div>
  <p class="body">Lorem Ipsum is simply dummy text of the printing and typesetting industry. Lorem Ipsum has been the industry's standard dummy text ever since the 1500s, when an unknown printer took a galley of type and scrambled it to make a type specimen book. It has survived not only five centuries, but also the leap into electronic typesetting, remaining essentially unchanged. Lorem Ipsum is simply dummy text of the printing and typesetting industry.</p>
  <div class="byline"><b>[Blog Psted By</b> Mara Dellow<b>]</b></div>
  <div class="share">Share This <i></i><i></i><i></i><i></i></div>
  <span class="more-info">More info [+]</span>
</article>

<aside class="abs contact">
  <h2>How to Contact Us At</h2>
  <h4>Phone:</h4>
  <p>Office: 1-877-555-0142 or 603-555-0187<br>Cell: 603-555-0129<br>Fax: 603-555-0156</p>
  <h4 style="margin-top:12px">Mail:</h4>
  <p>42 Larchmere Rd.,<br>Fenwick Falls, NH 03099</p>
  <p style="margin-top:15px">EMail<br><a>dana@harrowfieldcover.example</a></p>
</aside>

<div class="abs rule-dashed"></div>

<section class="abs testimonial">
  <h2>Testimonial</h2>
  <p>Lorem Ipsum is simply dummy text of the printing and typesetting industry. Lorem Ipsum has been the industry's standard dummy text ever since the 1500s, when an unknown printer took a galley of type and scrambled</p>
</section>
<svg class="abs quote-tail" width="48" height="32" viewBox="0 0 48 32" aria-hidden="true">
  <path d="M0 0 L26 0 L30 28 Z" fill="#8e0535"/>
  <circle cx="32" cy="20" r="11" fill="none" stroke="#ccc" stroke-width="2"/>
  <circle cx="32" cy="20" r="5" fill="none" stroke="#ccc" stroke-width="2"/>
</svg>
<div class="abs attribution">Owen Taskert, Fenwick Falls, NH</div>

<footer class="abs site-footer">
  <span>HOME</span><span>|</span><span>PRODUCTS</span><span>|</span><span>ABOUT US</span><span>|</span><span>NEWS/BLOG</span><span>|</span><span>CONTACT US</span>
</footer>

</body>
</html>
```